Design a Flyer for Christmas kids party

We own a cafe in a garden centre and organising a children's Christmas Activity/Craft morning.
There will be craft activities including 'make your xmas dexoration, create your own Christmas placemat and also a session where the children can design their own Christmas cupcake. party food for the kids and morning tea packages for the mum/carer.

needs to be eye catching and printable on a5, a4 and a3.

Dates and our logo can be provided with further text detail including dates etc

```html
<!DOCTYPE html>
<html lang="en">
<head>
<meta charset="utf-8">
<title>Christmas Party Flyer</title>
<link rel="stylesheet" href="https://fonts.googleapis.com/css2?family=Alfa+Slab+One&family=Arimo:wght@400;700&display=swap">
<style>
  :root {
    --red-core: #e3352c;
    --red-edge: #9c0d18;
    --banner-yellow: #f8ec1c;
    --banner-fold: #d9c30c;
    --title-red: #d8141e;
    --title-yellow: #f7e81a;
    --panel-pink: #f9dcd4;
    --ink: #111111;
    --logo-white: #ffffff;
  }
  * { box-sizing: border-box; margin: 0; padding: 0; }
  html, body { width: 847px; height: 1200px; overflow: hidden; background: #ffffff; }
  .flyer {
    position: relative;
    width: 847px;
    height: 1200px;
    overflow: hidden;
    background: radial-gradient(ellipse 70% 60% at 50% 45%, var(--red-core) 0%, #c81f24 55%, var(--red-edge) 100%);
    font-family: "Arimo", Arial, sans-serif;
    color: var(--ink);
  }
  .children-art {
    position: absolute;
    left: 36px; top: 0;
    width: 800px; height: 370px;
    border-radius: 0 0 200px 200px;
    background: linear-gradient(180deg, rgba(120, 70, 50, 0.45) 0%, rgba(240, 190, 150, 0.45) 45%, rgba(150, 120, 200, 0.45) 100%);
  }
  .banner {
    position: absolute;
    left: 0; top: 0;
    width: 847px; height: 600px;
  }
  .banner .fold { fill: var(--banner-fold); }
  .banner .band { fill: var(--banner-yellow); }
  .banner .headline {
    font-family: "Alfa Slab One", Georgia, serif;
    font-size: 80px;
    fill: var(--title-red);
    stroke: #a80c14;
    stroke-width: 1.5px;
  }
  .party-title {
    position: absolute;
    left: 0; top: 535px;
    width: 847px;
    text-align: center;
    font-family: "Alfa Slab One", Georgia, serif;
    font-size: 136px;
    line-height: 1;
    letter-spacing: 10px;
    color: var(--title-yellow);
    text-shadow: 0 2px 0 #c9a800;
  }
  .celebration-art {
    position: absolute;
    left: 0; top: 1000px;
    width: 847px; height: 200px;
    border-radius: 100px 100px 0 0;
    background: linear-gradient(180deg, rgba(240, 190, 80, 0.5) 0%, rgba(220, 90, 140, 0.5) 55%, rgba(90, 150, 220, 0.5) 100%);
  }
  .details {
    position: absolute;
    left: 34px; top: 709px;
    width: 784px; height: 279px;
    border-radius: 40px;
    background: var(--panel-pink);
    padding: 22px 0 0 29px;
  }
  .details .label { font-weight: 700; font-size: 20px; line-height: 36px; }
  .details .activities { list-style: none; padding-left: 28px; }
  .details .activities li { font-size: 19px; line-height: 35px; }
  .details .catering { font-size: 17px; line-height: 32px; margin-left: -2px; }
  .logo-box {
    position: absolute;
    left: 529px; top: 35px;
    width: 133px; height: 140px;
    background: var(--logo-white);
    display: flex; align-items: center; justify-content: center;
    font-size: 19px;
  }
</style>
</head>
<body>
<main class="flyer">
  <div class="children-art" role="img" aria-label="Illustration of four smiling children with arms around each other"></div>

  <svg class="banner" viewBox="0 0 847 600">
    <path class="fold" d="M18 420 L95 405 L95 500 L18 515 L45 468 Z"/>
    <path class="fold" d="M760 420 L842 432 L815 488 L842 565 L760 552 Z"/>
    <path class="band" d="M60 385 Q423 290 800 395 L800 500 Q423 395 60 482 Z"/>
    <path id="headline-curve" d="M92 462 Q423 372 775 468" fill="none"/>
    <text class="headline"><textPath href="#headline-curve" textLength="683" lengthAdjust="spacingAndGlyphs">CHRISTMAS</textPath></text>
  </svg>

  <h1 class="party-title">PARTY</h1>

  <div class="celebration-art" role="img" aria-label="Illustration of party balloons, party hats, streamers and wrapped gifts"></div>

  <section class="details">
    <p class="label">Time &amp; date</p>
    <p class="label">Place</p>
    <p class="label">Activities</p>
    <ul class="activities">
      <li>Make your own Christmas decoration</li>
      <li>Create your own Christmas placemat</li>
      <li>Design your own Christmas cupcake</li>
    </ul>
    <p class="catering">Party food for the kids and morning tea packages for the mum/carers</p>
    <div class="logo-box">LOGO</div>
  </section>
</main>
</body>
</html>
```